Attorney Website Design

I need a top quality attorney website layout designed. Here are some examples of what I feel are great websites:
http://www.quellmarstonseparationlaw.com/
http://www.vandriclegalgroup.com/
http://www.pobelaw.com/
http://www.harrowvaleaccusedcounselhq.com/
http://www.tzlegal.com/
http://www.brookhollowtrialjusticeoffice.com/
http://www.orvynchargedcounsel.com/
http://www.tzlegal.com/
What we like about these sites:
• The different layers
• Subtle designs, textures, curves
• 3 dimensional
• Floating effects
• Prominent phone number
• Location of Areas of Practice
• Request A Consultation Prominent
• Right side bar with practice areas
• Badges
• Clear Calls to Action
• Dynamic/Staying Top navigation when you scroll
The project will be for a home page and then also an interior page (should be similar to home page).
Updates
I want to make it understood I am looking for a design which is not a typical "template" site which I can find anywhere for $50. This budget and project is for a "Custom" website design. Please submit designs similar in quality to the samples links I have posted. Creativity is a MUST! The best way to explain this is, I want a design that I can feel it unique and original, not something that looks like 95% of all websites out there.
Neil
I just wanted everyone to know that so far I am not to pleased with any of the designs. I am not looking for cut/pasting of other peoples websites but ORIGINAL and CREATIVE work.
Reason: Weekend + Holiday extension.
Reason: Need more designs
Industry/Entity Type
Attorney

```html
<!DOCTYPE html>
<html lang="en">
<head>
<meta charset="utf-8">
<title>HarlowmereAttornies.com – Why Choose Us</title>
<link href="https://fonts.googleapis.com/css2?family=Open+Sans:ital,wght@0,400;0,600;0,700;0,800;1,400;1,600&display=swap" rel="stylesheet">
<style>
:root{
  --charcoal:#2b2b2b;
  --black:#000;
  --yellow:#ffcc00;
  --yellow-deep:#e5b800;
  --yellow-dark:#c9a200;
  --teal:#7cc8c2;
  --grey:#8a8a8a;
  --grey-light:#bdbdbd;
  --white:#fff;
  --tile:#f5f5f5;
  --red:#f03c1e;
}
*{box-sizing:border-box;margin:0;padding:0}
html,body{width:1200px;height:1080px;overflow:hidden}
body{font-family:"Open Sans",Arial,sans-serif;background:var(--black);position:relative;color:var(--white)}
.abs{position:absolute}
.intro{left:0;top:0;width:1200px;height:255px;background:var(--charcoal);text-align:center}
.intro h1{position:absolute;top:-14px;width:100%;font-size:30px;font-weight:800;color:var(--yellow);letter-spacing:1px}
.intro p{position:absolute;top:32px;width:100%;font-size:10.5px;line-height:16.6px}
.intro strong{font-weight:700}
.photo{border-radius:4px}
.photo-left{left:135px;top:173px;width:240px;height:170px;background:linear-gradient(90deg,#d8d4cc 0%,#a59c8e 45%,#3a1e16 75%,#8a2a18 100%)}
.photo-right{left:823px;top:172px;width:240px;height:170px;background:linear-gradient(135deg,#2c1a14 0%,#7a3424 40%,#b8533a 65%,#e6e2dc 100%)}
.photo-center{left:375px;top:128px;width:448px;height:248px;background:radial-gradient(ellipse at 60% 60%,#8a4a28 0%,#4a2a2e 45%,#2a2a44 100%);box-shadow:0 4px 14px rgba(0,0,0,.5)}
.section-title{font-size:13.5px;font-weight:700}
.why-title{left:131px;top:422px;color:var(--grey)}
.why-list{left:133px;top:462px;list-style:none;font-size:10.5px;color:var(--grey)}
.why-list li{height:20.8px;display:flex;align-items:center;gap:5px}
.why-list svg{width:9px;height:9px}
.lead{left:388px;top:419px;font-size:10.5px;line-height:20px;color:var(--grey);white-space:nowrap}
.lead a{color:var(--yellow);text-decoration:underline;font-weight:600}
.stats{left:370px;top:500px}
.stat-label{position:absolute;font-size:13px;font-weight:700;color:var(--grey-light);text-align:center;width:110px;top:66px}
.say-title{left:849px;top:422px;color:var(--yellow)}
.quote{left:851px;top:458px;width:216px;height:95px;background:var(--tile);border-radius:2px;padding:8px 13px;font-size:10.3px;line-height:19.5px;color:#777;white-space:nowrap}
.quote em{font-style:italic}
.quote-tail{left:866px;top:553px}
.quote-author{left:899px;top:558px;font-size:13.5px;font-weight:600;color:var(--grey)}
.clients-title{left:131px;top:630px;color:var(--yellow)}
.rule{left:266px;top:640px;width:705px;height:1px;background:#bbb}
.rule-dot{left:263px;top:637px;width:7px;height:7px;border-radius:50%;background:var(--white)}
.nav-btn{top:624px;width:32px;height:32px;border-radius:2px;display:flex;align-items:center;justify-content:center}
.nav-prev{left:987px;background:#9a9a9a}
.nav-next{left:1034px;background:var(--yellow)}
.client-tile{top:688px;width:136px;height:72px;background:var(--tile);border-radius:2px;display:flex;align-items:center;justify-content:center;gap:6px;font-size:16px;font-weight:700;color:#777}
.client-tile i{width:10px;height:10px;border-radius:50%;background:#999;display:block}
.footer{left:0;top:800px;width:1200px;height:240px;background:var(--yellow)}
.footer-bar{left:0;top:1040px;width:1200px;height:40px;background:var(--yellow-deep)}
.brand{left:134px;top:833px;font-size:21px;font-weight:700;color:var(--white);white-space:nowrap}
.about{left:135px;top:877px;font-size:10.5px;line-height:18.6px;color:var(--white);white-space:nowrap}
.contact{left:135px;font-size:10.5px;color:var(--white);display:flex;align-items:center;white-space:nowrap}
.contact span{width:48px}
.contact b{font-size:16px;font-style:italic;font-weight:600}
.col-title{top:836px;font-size:16px;font-weight:700;color:#222}
.links{top:877px;list-style:none;font-size:10.5px;color:var(--white)}
.links li{height:18.8px;display:flex;align-items:center;gap:8px}
.dev{left:771px;display:flex;gap:14px}
.thumb{width:56px;height:56px;background:var(--yellow-dark);border-radius:2px;display:flex;align-items:center;justify-content:center}
.dev p{font-size:10.5px;line-height:15px;color:var(--white);width:210px;margin-top:-1px}
.dev small{display:block;color:#a88600;font-size:10.5px;margin-top:1px}
.social{right:140px;top:1052px;display:flex;gap:16px;font-size:12px;font-weight:700;color:var(--white)}
</style>
</head>
<body>

<section class="abs intro">
  <h1>WHY CHOOSE US?</h1>
  <p>With an immense library of knowledge and esteemed clients under our blet, we strive to provide swift action and affirmative solutions to all our clients.<br>Our key focus areas are in:<br><strong>Criminal Defense</strong><br><strong>Family Law</strong><br><strong>Personal Injury</strong></p>
</section>

<div class="abs photo photo-left" role="img" aria-label="Statue of justice with law books"></div>
<div class="abs photo photo-right" role="img" aria-label="Law office lounge with white armchairs"></div>
<div class="abs photo photo-center" role="img" aria-label="Judge's gavel on a wooden desk"></div>

<h2 class="abs section-title why-title">Why Choose Us ?</h2>
<ul class="abs why-list">
  <li><svg viewBox="0 0 10 10"><path d="M1 5h7M5 2l3 3-3 3" stroke="#f03c1e" stroke-width="2" fill="none"/></svg>Quisque at massa ipsum</li>
  <li><svg viewBox="0 0 10 10"><path d="M1 5h7M5 2l3 3-3 3" stroke="#f03c1e" stroke-width="2" fill="none"/></svg>Maecenas a lorem augue, egestas</li>
  <li><svg viewBox="0 0 10 10"><path d="M1 5h7M5 2l3 3-3 3" stroke="#f03c1e" stroke-width="2" fill="none"/></svg>Cras vitae felis at lacus eleifend</li>
  <li><svg viewBox="0 0 10 10"><path d="M1 5h7M5 2l3 3-3 3" stroke="#f03c1e" stroke-width="2" fill="none"/></svg>Etiam auctor diam pellentesque</li>
  <li><svg viewBox="0 0 10 10"><path d="M1 5h7M5 2l3 3-3 3" stroke="#f03c1e" stroke-width="2" fill="none"/></svg>Nulla ac massa at dolor</li>
  <li><svg viewBox="0 0 10 10"><path d="M1 5h7M5 2l3 3-3 3" stroke="#f03c1e" stroke-width="2" fill="none"/></svg>Condimentum eleifend vitae vitae</li>
</ul>

<p class="abs lead">Curabitur quis nisl in leo euismod venenatis eu in diam. Etiam auctor diam pellentesque<br>lectus <a>vehicula mattis</a>. Nulla ac massa at dolor condimentum eleifend vitae vitae urna.</p>

<div class="abs stats">
  <svg width="460" height="60" viewBox="0 0 460 60" style="position:absolute;left:0;top:0">
    <g font-family="Open Sans, sans-serif" font-weight="700" font-size="23" fill="#bdbdbd" text-anchor="middle">
      <g transform="translate(57,50)">
        <path d="M-42 0A42 42 0 0 1 42 0" stroke="#7cc8c2" stroke-width="12" fill="none" pathLength="100"/>
        <path d="M-42 0A42 42 0 0 1 42 0" stroke="#ffcc00" stroke-width="12" fill="none" pathLength="100" stroke-dasharray="50 100"/>
        <text y="-2">50</text>
      </g>
      <g transform="translate(171,50)">
        <path d="M-42 0A42 42 0 0 1 42 0" stroke="#7cc8c2" stroke-width="12" fill="none" pathLength="100"/>
        <path d="M-42 0A42 42 0 0 1 42 0" stroke="#ffcc00" stroke-width="12" fill="none" pathLength="100" stroke-dasharray="70 100"/>
        <text y="-2">70</text>
      </g>
      <g transform="translate(285,50)">
        <path d="M-42 0A42 42 0 0 1 42 0" stroke="#7cc8c2" stroke-width="12" fill="none" pathLength="100"/>
        <path d="M-42 0A42 42 0 0 1 42 0" stroke="#ffcc00" stroke-width="12" fill="none" pathLength="100" stroke-dasharray="80 100"/>
        <text y="-2">80</text>
      </g>
      <g transform="translate(400,50)">
        <path d="M-42 0A42 42 0 0 1 42 0" stroke="#ffcc00" stroke-width="12" fill="none"/>
        <text y="-2">100</text>
      </g>
    </g>
  </svg>
  <span class="stat-label" style="left:3px">CLIENTS</span>
  <span class="stat-label" style="left:117px">CASES</span>
  <span class="stat-label" style="left:232px">SETTLEMENTS</span>
  <span class="stat-label" style="left:347px">FEEDBACK</span>
</div>

<h2 class="abs section-title say-title">What Client’s Say ?</h2>
<blockquote class="abs quote"><em>Curabitur quis nisl in leo euismod<br>venenatis eu in diam. Etiam auctor diam<br>pellentesque lectus vehicula mattis.</em> Nulla<br>ac massa at dolor condimentum</blockquote>
<svg class="abs quote-tail" width="21" height="21" viewBox="0 0 21 21"><path d="M0 0H21V21Z" fill="#f5f5f5"/></svg>
<span class="abs quote-author">Jhon Doe</span>

<h2 class="abs section-title clients-title">Our Happy Clients</h2>
<div class="abs rule"></div>
<div class="abs rule-dot"></div>
<div class="abs nav-btn nav-prev"><svg width="12" height="14" viewBox="0 0 12 14"><path d="M9 1L3 7l6 6" stroke="#fff" stroke-width="3" fill="none"/></svg></div>
<div class="abs nav-btn nav-next"><svg width="12" height="14" viewBox="0 0 12 14"><path d="M3 1l6 6-6 6" stroke="#fff" stroke-width="3" fill="none"/></svg></div>

<div class="abs client-tile" style="left:131px"><i></i>Corvane</div>
<div class="abs client-tile" style="left:291px"><i></i>Corvane</div>
<div class="abs client-tile" style="left:451px"><i></i>Corvane</div>
<div class="abs client-tile" style="left:611px"><i></i>Corvane</div>
<div class="abs client-tile" style="left:771px"><i></i>Corvane</div>
<div class="abs client-tile" style="left:931px"><i></i>Corvane</div>

<footer>
  <div class="abs footer"></div>
  <div class="abs brand">HarlowmereAttornies.com</div>
  <p class="abs about">Lorem ipsum dolor sit amet, consectetur adipiscing elit. Nam<br>viverra euismod odio, gravida pellentesque urna varius vitae.<br>Sed dui lorem, adipiscing in adipiscing et, interdum nec .</p>
  <div class="abs contact" style="top:950px"><span>Phone:</span><b>1(203)555-0148</b></div>
  <div class="abs contact" style="top:974px"><span>e-mail:</span><b>info@harlowmereattornies.com</b></div>

  <h3 class="abs col-title" style="left:452px">Company</h3>
  <ul class="abs links" style="left:471px">
    <li>›<span>About</span></li><li>›<span>FAQ</span></li><li>›<span>Contact</span></li><li>›<span>Terms</span></li><li>›<span>Privacy</span></li><li>›<span>Testimonials</span></li>
  </ul>

  <h3 class="abs col-title" style="left:612px">Community</h3>
  <ul class="abs links" style="left:631px">
    <li>›<span>Blog</span></li><li>›<span>Forum</span></li><li>›<span>Support</span></li><li>›<span>Newsletter</span></li>
  </ul>

  <h3 class="abs col-title" style="left:772px">Developments</h3>
  <div class="abs dev" style="top:876px">
    <div class="thumb" role="img" aria-label="News article thumbnail"></div>
    <p>Lorem ipsum dolor sit amet, consectetur adipiscing elit<small>26 May, 2013</small></p>
  </div>
  <div class="abs dev" style="top:948px">
    <div class="thumb" role="img" aria-label="News article thumbnail"></div>
    <p>Lorem ipsum dolor sit amet, consectetur adipiscing elit<small>26 May, 2013</small></p>
  </div>

  <div class="abs footer-bar"></div>
  <nav class="abs social"><span>Lumo</span><span>Vexa</span><span>Chirra</span><span>Rivo</span></nav>
</footer>

</body>
</html>
```